Introduction Post card

Harbourline Doors
27 Varnel Road
Ruthven Ontario
Gus@harbourlinedoorsco.net
519-555-0143

Dear Leamington Residents

We are excited to announce the launch of Harbourline Doors, your new local source for high-quality windows, doors, and garage doors! As a dedicated member of this community, we are committed to providing exceptional products and services that enhance the beauty and functionality of your home or business.

At Harbourline Doors, we understand that choosing the right windows and doors is essential for energy efficiency, security, and style. That’s why we offer a wide selection of premium products tailored to meet your unique needs. Our expert team is here to guide you through the selection process, ensuring you find the perfect fit for your space.

Our services don’t stop at providing quality products. We pride ourselves on our professional installation process, ensuring that every project is completed with precision and care. Customer satisfaction is our top priority, and we strive to exceed your expectations with every interaction.

We invite you to visit our showroom or contact us to learn more about our offerings. Whether you’re looking to upgrade your home’s curb appeal or enhance its security, we are here to help. Together, let’s make our community a more beautiful place!

Thank you for considering Harbourline Doors for your window, door, and garage door needs. We look forward to serving you!

Warm regards,

Gus
Sales Manager
Harbourline Doors
https://harbourlinedoorsco.net/

```html
<!DOCTYPE html>
<html lang="en">
<head>
<meta charset="utf-8">
<title>Harbourline Doors – Introduction Postcard</title>
<link href="https://fonts.googleapis.com/css2?family=Roboto:ital,wght@0,300;0,400;0,700;0,900;1,400&family=Roboto+Condensed:ital,wght@0,700;1,400&display=swap" rel="stylesheet">
<style>
  :root {
    --stage: #b1b1b1;
    --paper: #ffffff;
    --charcoal: #48474a;
    --orange: #e5622b;
    --ink: #3c3c3c;
    --rule: #6b6b6b;
    --sky-top: #5f9fd8;
    --sky-low: #cfe3f1;
    --lawn: #58a83a;
  }
  * { box-sizing: border-box; margin: 0; padding: 0; }
  html, body { width: 1133px; height: 1200px; overflow: hidden; }
  body {
    background: var(--stage);
    font-family: "Roboto", sans-serif;
    display: flex; flex-direction: column; align-items: center; justify-content: center; gap: 34px;
  }
  .card { position: relative; width: 770px; height: 550px; overflow: hidden; box-shadow: 0 6px 14px rgba(0,0,0,.25); }

  /* Back side */
  .card--back { background: var(--paper); color: var(--ink); }
  .letter { position: absolute; left: 28px; top: 26px; width: 448px; }
  .letter__greeting { font-family: "Roboto Condensed", sans-serif; font-style: italic; color: var(--orange); font-size: 15px; margin-bottom: 7px; }
  .letter p { font-weight: 300; font-size: 14px; line-height: 16.6px; text-align: justify; margin-bottom: 5px; }
  .letter__closing { margin-top: 9px; }
  .letter__signature { font-family: "Roboto Condensed", sans-serif; font-style: italic; color: var(--orange); font-size: 14.5px; line-height: 14.5px; margin-top: 8px; }
  .stamp-box { position: absolute; left: 647px; top: 27px; width: 96px; height: 121px; border: 1px solid var(--rule); }
  .address-line { position: absolute; left: 504px; width: 239px; height: 0; border-top: 1px solid var(--rule); }
  .back-band { position: absolute; left: 0; bottom: 0; }
  .back-url { position: absolute; left: 232px; width: 310px; top: 511px; text-align: center; color: var(--orange); font-size: 15px; }

  /* Front side */
  .card--front { background: var(--charcoal); color: #fff; }
  .front-art { position: absolute; inset: 0; }
  .brand { position: absolute; left: 27px; top: 98px; display: flex; align-items: center; gap: 9px;
    font-family: "Roboto Condensed", sans-serif; font-weight: 700; font-size: 24px; letter-spacing: .2px; }
  .brand__mark { width: 14px; height: 14px; background: #fff; }
  .headline { position: absolute; left: 27px; top: 188px; font-weight: 900; font-size: 44px; line-height: 45px; letter-spacing: .3px; }
  .tagline { position: absolute; left: 27px; top: 357px; font-weight: 500; font-size: 14.5px; line-height: 17px; }
  .phone { position: absolute; left: 27px; top: 412px; font-weight: 900; font-size: 37px; color: var(--orange); letter-spacing: 1.5px; }
  .contact { position: absolute; left: 27px; top: 462px; font-size: 14.5px; line-height: 20px; }
  .contact__row { display: flex; align-items: center; gap: 6px; }
  .contact__icon { width: 11px; height: 11px; flex: none; }
  .front-url { position: absolute; left: 250px; width: 300px; top: 519px; text-align: center; font-size: 15px; }
</style>
</head>
<body>

<section class="card card--back" aria-label="Postcard back">
  <div class="letter">
    <h2 class="letter__greeting">Dear Leamington Residents</h2>
    <p>We are excited to announce the launch of Harbourline Doors, your new local source for high-quality windows, doors, and garage doors! As a dedicated member of this community, we are committed to providing exceptional products and services that enhance the beauty and functionality of your home or business.</p>
    <p>At Harbourline Doors, we understand that choosing the right windows and doors is essential for energy efficiency, security, and style. That’s why we offer a wide selection of premium products tailored to meet your unique needs. Our expert team is here to guide you through the selection process, ensuring you find the perfect fit for your space.</p>
    <p>Our services don’t stop at providing quality products. We pride ourselves on our professional installation process, ensuring that every project is completed with precision and care. Customer satisfaction is our top priority, and we strive to exceed your expectations with every interaction.</p>
    <p>We invite you to visit our showroom or contact us to learn more about our offerings. Whether you’re looking to upgrade your home’s curb appeal or enhance its security, we are here to help. Together, let’s make our community a more beautiful place!</p>
    <p>Thank you for considering Harbourline Doors for your window, door, and garage door needs. We look forward to serving you!</p>
    <p class="letter__closing">Warm regards,</p>
    <div class="letter__signature">Gus<br>Sales Manager<br>Harbourline Doors</div>
  </div>
  <div class="stamp-box"></div>
  <div class="address-line" style="top:305px"></div>
  <div class="address-line" style="top:355px"></div>
  <div class="address-line" style="top:405px"></div>
  <div class="address-line" style="top:455px"></div>
  <svg class="back-band" width="770" height="550" viewBox="0 0 770 550" style="top:0">
    <polygon points="0,506 228,506 236,528 540,528 540,550 0,550" fill="var(--orange)"/>
    <polygon points="548,506 770,506 770,550 536,550" fill="var(--charcoal)"/>
  </svg>
  <div class="back-url">www.harbourlinedoorsco.net</div>
</section>

<section class="card card--front" aria-label="Postcard front">
  <svg class="front-art" width="770" height="550" viewBox="0 0 770 550">
    <defs>
      <linearGradient id="photoTones" x1="0" y1="0" x2="0" y2="1">
        <stop offset="0" stop-color="var(--sky-top)"/>
        <stop offset=".35" stop-color="var(--sky-low)"/>
        <stop offset=".55" stop-color="#c9b8a4"/>
        <stop offset=".68" stop-color="#8f9a8c"/>
        <stop offset=".75" stop-color="var(--lawn)"/>
        <stop offset="1" stop-color="#3f8f2a"/>
      </linearGradient>
    </defs>
    <rect x="200" y="0" width="570" height="550" fill="url(#photoTones)" role="img" aria-label="Photo of a modern two-storey house with wood and stone facade, large windows and a green lawn under a blue sky"/>
    <polygon points="0,0 217,0 352,400 330,550 0,550" fill="var(--charcoal)"/>
    <polygon points="0,354 340,354 354,394 0,394" fill="var(--orange)"/>
    <polygon points="0,550 0,548 210,536 240,550" fill="#f2f2f2"/>
    <polygon points="256,507 532,507 554,550 236,550" fill="var(--orange)"/>
  </svg>
  <div class="brand"><span class="brand__mark"></span>HARBOURLINE DOORS</div>
  <h1 class="headline">Elevate<br>Your Home with<br>Harbourline Doors!</h1>
  <div class="tagline">Your Trusted Source for Premium Windows,<br>Doors, and Garage Doors!</div>
  <div class="phone">519-555-0143</div>
  <div class="contact">
    <div class="contact__row">
      <svg class="contact__icon" viewBox="0 0 11 11"><rect width="11" height="11" rx="1.5" fill="var(--orange)"/><path d="M5.5 2a2.2 2.2 0 0 0-2.2 2.2c0 1.7 2.2 4.3 2.2 4.3s2.2-2.6 2.2-4.3A2.2 2.2 0 0 0 5.5 2zm0 3a.8.8 0 1 1 0-1.6.8.8 0 0 1 0 1.6z" fill="#fff"/></svg>
      27 Varnel Road, Ruthven, Ontario
    </div>
    <div class="contact__row">
      <svg class="contact__icon" viewBox="0 0 11 11"><rect width="11" height="11" rx="1.5" fill="var(--orange)"/><rect x="2.2" y="3.2" width="6.6" height="4.6" fill="none" stroke="#fff" stroke-width=".9"/><path d="M2.2 3.2l3.3 2.6 3.3-2.6" fill="none" stroke="#fff" stroke-width=".9"/></svg>
      Gus@harbourlinedoorsco.net
    </div>
  </div>
  <div class="front-url">www.harbourlinedoorsco.net</div>
</section>

</body>
</html>
```